KELVAR OIL BROCHURE

Design a brochure for Kelvar Oil and Gas Limited using the attached information.
An Overview / Background of the Business & Services

Kelvar Oil and Gas Limited (KOGL) is an oil and gas company dually incorporated under the laws of the Federal Republic of Nigeria. KOGL operations cover both the upstream and downstream activities of the oil and gas industry.

The company is led by a team of seasoned professionals with an excess of 28 years combined hands-on and top management experience in the industry. This is in addition to the wealth of experience and technology of our affiliates and technical partners.

KOGL was started to provide excellent, cost efficient, effective solutions and specialized operations for the oil and gas industry. It stated as a service company providing solutions in the environmental sector and has progressed to provide a comprehensive range of solutions in engineering, production, procurement and maintenance services.

Our key strength is the expertise of our staff, the vast experience of our technical partners, our vision and our commitment to our core values.

We are here to serve you better.

Vision Statement
Our vision is to be the gas and oil company of excellence and global leader in this sector.

Mission Statement
Our mission is to achieve our vision in the shortest possible time.

=================
Operations

Services
Kelvar Oil and Gas Limited is functional in both the downstream and upstream operation. Whatever your need, we have the expertise to offer solutions and guidance.

Our wide array of services includes:
 Pipeline and flow lines design, construction/installation, maintenance and emergency repairs.
 Maintenance and rehabilitation of platforms, gas compressor plants and flow stations.
 Installation & maintenance of steam and gas turbines, boilers & heat exchangers, fire water system, pumps, etc.
 Installation & maintenance of booster pumps and platform refurbishment.
 Engineering Design Services.
 Procurement Services.
 Provide experienced and professional technical Manpower
 Engineering Services (Mechanical, Civil and Electrical works)
 Environmental Services

We can execute fully integrated projects at remote locations supported by a satellite office. Our team work diligently to maximize clients’ return and avoid unplanned downtime. We have the requisite equipment to deliver value and quality.

Products
Equipment Hire
We use state of the art equipment to deliver prompt services according to specifications. We also support the industry and grow local capacity by offering equipment hire and lease services. We have in stock an array of pre-mobbed equipment, ready to be deployed for emergency and planned activity.

Show pictures of equipment (See attached pictures)

Materials
In conjunction with our partners we offer the following materials:

=================
Project Portfolio
In have delivered a number of quality and durable projects.

Show pictures of work done. (See attached pictures)

=======================
Corporate Culture

Quality Culture
Kelvar Oil and Gas Limited pride itself on its corporate quality culture. We feel strongly that quality goes beyond simply following procedures and meeting productivity expectations.

At every level of the company, we insist on taking quality focused action and transferring those values to our clients. The culture of quality is part of our environment. The end result is better communication, high-end services and products that function as promised.

Each member of the Kelvar team is empowered and expected to make good decisions based on the need to deliver quality and value.

Health, Safety and Environment (HSE)
Health, Safety and Environment (HSE) is a fundamental component of KOGL business principles and corporate culture. It is our priority to maintain safe and healthy working conditions by ensuring industrial and work area safety rules, regulations, laws, conditions and standard codes.

The company believes that effective management of HSE affairs not only protects staff and environment, but also contributes to the company’s success. Therefore, we regard it as important as the achievement of any other key business objective.

Our Core Values
At Kelvar Oil and Gas Limited we aim to be good corporate citizens in every area of our operations. We mold our actions around a corporate value guide that is central to all our decision making policy.

Our values are based on a commitment to the greater good of our employees, clients, and the safety and protection of the environments where we work. Investing in communities and groups in ways that are aligned with our values is part of our corporate policy. In addition, it is our culture to restore integrity for every services and products under our care.

While we operate the professional best practices in the oil and gas industry, our overriding core values include:
 To conduct KOGL businesses to the glory and pleasure of the Almighty God.
 To express the righteousness of God in all operations, products and services as our brand.
 To treat our staff as valued partners (co-owner) in the business.
 To work in such a way that will preserve the earth resources.

Partners
Our strategic partners were carefully selected for their industry knowledge about local conditions and international trends. They have the ability to provide comprehensive, effective support to our client. As a result of these relationships, Kelvar Oil and Gas Limited is able to deliver innovative technical solutions to the localities where it operates.

We use these strategic partnerships to unlock value in projects worldwide. They enable us to provide the latest technology and resources for future projects. Together we are able to use the full potential of our mutual resources to provide values for our clients.

Partners:
www.brantwellcord.example
www.morvilqexport.example
www.halden-pryce.example

Contact
Website: www.kelvaroilandgas.example
E-mail: info@kelvaroilandgas.example

Target Market(s)

The oil and gas community - oil and gas servicing companies, production companies, refinaries etc.

Industry/Entity Type

Business

Font styles to use
Serif
Script

Requirements
Must have
• Picture and photos. I have attached some pictures of completed work.
Nice to have
• Some nice photos from the net will be good

```html
<!DOCTYPE html>
<html lang="en">
<head>
<meta charset="utf-8">
<title>Kelvar Oil and Gas Limited — Brochure</title>
<link rel="stylesheet" href="https://fonts.googleapis.com/css2?family=Arimo:wght@400;700&display=swap">
<style>
  :root {
    --green-deep: #0d5a2c;
    --green: #17723a;
    --green-light: #1f8a45;
    --gold: #e8b417;
    --gold-text: #f2c12e;
    --blue: #1d3f8f;
    --white: #ffffff;
    --paper-bg: #e4e5e6;
    --rule: rgba(255,255,255,0.55);
  }
  * { box-sizing: border-box; margin: 0; padding: 0; }
  html, body {
    width: 1200px; height: 847px; overflow: hidden;
    background: var(--paper-bg);
    font-family: "Arimo", Arial, sans-serif;
  }
  .spread {
    position: absolute; left: 180px; top: 126px;
    width: 840px; height: 594px;
    display: flex;
    box-shadow: 0 6px 24px rgba(0,0,0,0.18);
  }
  .page { position: relative; width: 420px; height: 594px; overflow: hidden; }

  /* Back cover */
  .page--back {
    background: linear-gradient(160deg, var(--green-light) 0%, var(--green) 45%, var(--green-deep) 100%);
    color: var(--white);
  }
  .brand {
    display: flex; align-items: center; gap: 8px;
    font-weight: 700; letter-spacing: 0.5px;
  }
  .brand__dot { width: 12px; height: 12px; border-radius: 50%; background: var(--gold); }
  .page--back .brand { position: absolute; left: 110px; top: 92px; font-size: 26px; color: var(--white); }
  .partners-copy { position: absolute; left: 48px; top: 205px; width: 330px; }
  .partners-copy h2 {
    font-weight: 400; font-size: 13px; color: var(--gold-text); margin-bottom: 2px;
  }
  .partners-copy p {
    font-size: 10px; line-height: 1.32; text-align: justify; margin-bottom: 11px;
  }
  .back-rule {
    position: absolute; left: 48px; top: 420px; width: 330px; height: 1px; background: var(--rule);
  }
  .back-footer {
    position: absolute; left: 48px; top: 432px; width: 330px;
    display: flex; gap: 26px; font-size: 10px; line-height: 1.35;
  }
  .back-footer .partner-list { padding-top: 14px; }

  /* Front cover */
  .page--front { background: var(--white); }
  .front-art { position: absolute; inset: 0; }
  .page--front .brand {
    position: absolute; left: 0; right: 0; top: 42px; justify-content: center;
    font-size: 24px; color: var(--green);
  }
  .intro {
    position: absolute; left: 36px; right: 36px; top: 350px;
    color: var(--white); font-size: 10px; line-height: 1.3; text-align: center;
  }
  .intro__url {
    position: absolute; left: 0; right: 0; top: 420px;
    text-align: center; font-size: 10px; color: var(--gold-text);
  }
</style>
</head>
<body>
  <main class="spread">
    <section class="page page--back">
      <div class="brand"><span class="brand__dot"></span><span>Kelvar Oil &amp; Gas</span></div>

      <article class="partners-copy">
        <h2>Partners</h2>
        <p>Our strategic partners were carefully selected for their industry knowledge about local conditions and international trends. They have the ability to provide comprehensive, effective support to our client. As a result of these relationships, Kelvar Oil and Gas Limited is able to deliver innovative technical solutions to the localities where it operates.</p>
        <p>We use these strategic partnerships to unlock value in projects worldwide. They enable us to provide the latest technology and resources for future projects. Together we are able to use the full potential of our mutual resources to provide values for our clients.</p>
      </article>

      <div class="back-rule"></div>

      <footer class="back-footer">
        <div class="partner-list">
          Partners:<br>
          www.brantwellcord.example<br>
          www.morvilqexport.example<br>
          www.halden-pryce.example
        </div>
        <div class="contact">
          Contact<br>
          Website: www.kelvaroilandgas.example<br>
          E-mail: info@kelvaroilandgas.example
        </div>
      </footer>
    </section>

    <section class="page page--front">
      <svg class="front-art" width="420" height="594" viewBox="0 0 420 594" aria-hidden="false">
        <path d="M0 300 Q250 332 420 282 L420 594 L0 594 Z" fill="#137039"/>
        <path d="M0 116 Q210 86 420 112 L420 120 Q210 94 0 124 Z" fill="#17723a"/>
        <path d="M0 124 Q210 94 420 120 L420 126 Q210 100 0 130 Z" fill="#e8b417"/>
        <g role="img" aria-label="Photo of a smiling oil field worker in a hard hat and safety vest at a plant site">
          <path d="M0 132 Q210 102 420 128 L420 268 Q250 318 0 286 Z" fill="#8a7d6a"/>
        </g>
        <path d="M0 286 Q250 318 420 268 L420 276 Q250 326 0 293 Z" fill="#e8b417"/>
        <path d="M0 293 Q250 326 420 276 L420 282 Q250 332 0 299 Z" fill="#1d3f8f"/>
        <path d="M0 299 Q250 332 420 282 L420 285 Q250 336 0 302 Z" fill="#ffffff"/>
      </svg>

      <div class="brand"><span class="brand__dot"></span><span>Kelvar Oil &amp; Gas</span></div>

      <p class="intro">Kelvar Oil and Gas Limited (KOGL) is an oil and gas company dually incorporated under the laws of the Federal Republic of Nigeria. KOGL operations cover both the upstream and downstream activities of the oil and gas industry.</p>
      <p class="intro__url">www.kelvaroilandgas.example</p>
    </section>
  </main>
</body>
</html>
```